Stationary and design update for my brand

I need new letterhead, a new business card, business envelope design, new keynote and powerpoint branded slides (16x9). I have logo samples in various styles and brand standards for fonts and colors.

Font styles to use
Sans Serif

```html
<!DOCTYPE html>
<html lang="en">
<head>
<meta charset="utf-8">
<title>Ridgeline Stationery Set</title>
<link rel="stylesheet" href="https://fonts.googleapis.com/css2?family=Questrial&display=swap">
<style>
  :root {
    --orange: #f39419;
    --grey: #7b7b7b;
    --ink: #3a3a3a;
    --paper: #f5f5f5;
    --paper-shade: #e4e4e4;
    --backdrop: #ebe8e3;
    --sans: "Questrial", sans-serif;
  }
  * { box-sizing: border-box; margin: 0; padding: 0; }
  html, body { width: 1200px; height: 800px; overflow: hidden; }
  body { background: var(--backdrop); position: relative; font-family: var(--sans); color: var(--ink); }

  .sheet {
    position: absolute;
    background: var(--paper);
    box-shadow: 0 6px 18px rgba(0,0,0,.15);
    overflow: hidden;
  }
  .letterhead { left: 60px; top: 115px; width: 440px; height: 569px; }
  .envelope { left: 560px; top: 115px; width: 600px; height: 260px; }
  .card { width: 280px; height: 160px; top: 430px; }
  .card-back { left: 560px; background: var(--orange); }
  .card-front { left: 880px; }

  .ridge-area { position: absolute; pointer-events: none; }
  .letterhead .ridge-area {
    right: 0; bottom: 0; width: 320px; height: 360px;
    background: radial-gradient(ellipse at 100% 100%, var(--paper-shade) 0%, rgba(228,228,228,0) 70%);
  }
  .envelope .ridge-area {
    right: 0; top: 0; width: 300px; height: 260px;
    background: radial-gradient(ellipse at 100% 0%, var(--paper-shade) 0%, rgba(228,228,228,0) 70%);
  }
  .card-front .ridge-area {
    right: 0; bottom: 0; width: 130px; height: 100px;
    background: radial-gradient(ellipse at 100% 100%, var(--paper-shade) 0%, rgba(228,228,228,0) 70%);
  }
  .card-back .ridge-area {
    right: 0; bottom: 0; width: 130px; height: 100px;
    background: radial-gradient(ellipse at 100% 100%, rgba(255,255,255,.28) 0%, rgba(255,255,255,0) 70%);
  }

  .wordmark {
    position: absolute;
    font-family: var(--sans);
    color: var(--orange);
    letter-spacing: .12em;
    line-height: 1;
    white-space: nowrap;
  }
  .letterhead .wordmark { top: 60px; left: 50%; transform: translateX(-50%); font-size: 28px; }
  .envelope .wordmark { top: 30px; left: 30px; font-size: 22px; }
  .card-back .wordmark { color: #fff; font-size: 28px; top: 56px; left: 50%; transform: translateX(-50%); }
  .card-back .tagline {
    position: absolute; top: 94px; width: 100%; text-align: center;
    color: #fff; font-size: 7px; letter-spacing: .14em; text-transform: uppercase;
  }
  .card-front .wordmark { font-size: 16px; top: 18px; right: 20px; }

  .contact { position: absolute; display: flex; flex-direction: column; gap: 3px; font-size: var(--fs); }
  .letterhead .contact { left: 28px; bottom: 34px; --fs: 10px; }
  .envelope .contact { left: 30px; bottom: 26px; --fs: 8px; }
  .card-front .contact { left: 16px; bottom: 14px; --fs: 6.5px; }

  .contact-row { display: flex; align-items: center; gap: 5px; }
  .contact-icon { width: calc(var(--fs) * 1.2); height: calc(var(--fs) * 1.2); fill: var(--ink); flex: none; }
  .contact-value {
    padding: calc(var(--fs) * .3) calc(var(--fs) * 1.6) calc(var(--fs) * .3) calc(var(--fs) * .5);
    letter-spacing: .06em;
    text-transform: uppercase;
    white-space: nowrap;
    clip-path: polygon(0 0, calc(100% - var(--fs)) 0, 100% 100%, 0 100%);
  }
  .contact-value.is-grey { background: var(--grey); color: #fff; }
  .contact-value.is-orange { background: var(--orange); color: #fff; }
  .contact-value.is-plain { border-bottom: 1px solid var(--ink); clip-path: none; }
  .company-bar {
    margin-left: calc(var(--fs) * 1.2 + 5px);
    background: var(--grey); color: #fff;
    letter-spacing: .05em;
    white-space: nowrap;
    padding: calc(var(--fs) * .35) calc(var(--fs) * 2) calc(var(--fs) * .35) calc(var(--fs) * .5);
    clip-path: polygon(0 0, calc(100% - var(--fs)) 0, 100% 100%, 0 100%);
  }

  .person { position: absolute; left: 16px; top: 50px; }
  .person-name { color: var(--orange); font-size: 8.5px; letter-spacing: .05em; text-transform: uppercase; display: flex; align-items: center; gap: 4px; white-space: nowrap; }
  .person-name svg { width: 9px; height: 9px; fill: var(--orange); }
  .person-role { font-size: 6.5px; margin-left: 13px; margin-top: 3px; letter-spacing: .06em; text-transform: uppercase; }
</style>
</head>
<body>
<svg width="0" height="0" style="position:absolute">
  <defs>
    <symbol id="icon-phone" viewBox="0 0 24 24"><path d="M6.6 10.8a15 15 0 0 0 6.6 6.6l2.2-2.2c.3-.3.7-.4 1-.2 1.1.4 2.3.6 3.6.6.6 0 1 .4 1 1V20c0 .6-.4 1-1 1A17 17 0 0 1 3 4c0-.6.4-1 1-1h3.5c.6 0 1 .4 1 1 0 1.3.2 2.5.6 3.6.1.3 0 .7-.2 1z"/></symbol>
    <symbol id="icon-mail" viewBox="0 0 24 24"><path d="M2 5h20v14H2zm2 2v.5l8 5 8-5V7zm0 2.8V17h16V9.8l-8 5z"/></symbol>
    <symbol id="icon-pin" viewBox="0 0 24 24"><path d="M12 2a7 7 0 0 0-7 7c0 5 7 13 7 13s7-8 7-13a7 7 0 0 0-7-7zm0 9.5A2.5 2.5 0 1 1 12 6.5a2.5 2.5 0 0 1 0 5z"/></symbol>
    <symbol id="icon-person" viewBox="0 0 24 24"><circle cx="12" cy="7" r="5"/><path d="M2 22c0-5.5 4.5-9 10-9s10 3.5 10 9z"/></symbol>
  </defs>
</svg>

<section class="sheet letterhead">
  <div class="ridge-area" role="img" aria-label="Faint grey mountain ridge decoration"></div>
  <div class="wordmark">RIDGELINE</div>
  <div class="contact">
    <div class="contact-row"><svg class="contact-icon"><use href="#icon-phone"/></svg><span class="contact-value is-grey">(555) 210-4830</span></div>
    <div class="contact-row"><svg class="contact-icon"><use href="#icon-mail"/></svg><span class="contact-value is-orange">elias@ridgelinecbc.com</span></div>
    <div class="contact-row"><svg class="contact-icon"><use href="#icon-pin"/></svg><span class="contact-value is-plain">4810 Alder Crest Dr, Plano, TX 75024</span></div>
    <div class="company-bar">Ridgeline Coaching and Behavioral Consulting LLC</div>
  </div>
</section>

<section class="sheet envelope">
  <div class="ridge-area" role="img" aria-label="Faint grey mountain ridge decoration"></div>
  <div class="wordmark">RIDGELINE</div>
  <div class="contact">
    <div class="contact-row"><svg class="contact-icon"><use href="#icon-phone"/></svg><span class="contact-value is-grey">(555) 210-4830</span></div>
    <div class="contact-row"><svg class="contact-icon"><use href="#icon-mail"/></svg><span class="contact-value is-orange">elias@ridgelinecbc.com</span></div>
    <div class="contact-row"><svg class="contact-icon"><use href="#icon-pin"/></svg><span class="contact-value is-plain">4810 Alder Crest Dr, Plano, TX 75024</span></div>
  </div>
</section>

<section class="sheet card card-back">
  <div class="ridge-area" role="img" aria-label="Faint light mountain ridge decoration"></div>
  <div class="wordmark">RIDGELINE</div>
  <div class="tagline">Coaching and Behavioral Consulting</div>
</section>

<section class="sheet card card-front">
  <div class="ridge-area" role="img" aria-label="Faint grey mountain ridge decoration"></div>
  <div class="wordmark">RIDGELINE</div>
  <div class="person">
    <div class="person-name"><svg><use href="#icon-person"/></svg>Elias Marlow-Bennett, DMin, PCC</div>
    <div class="person-role">Owner / Trainer / Coach / Consultant</div>
  </div>
  <div class="contact">
    <div class="contact-row"><svg class="contact-icon"><use href="#icon-phone"/></svg><span class="contact-value is-grey">(555) 210-4830</span></div>
    <div class="contact-row"><svg class="contact-icon"><use href="#icon-mail"/></svg><span class="contact-value is-orange">elias@ridgelinecbc.com</span></div>
    <div class="contact-row"><svg class="contact-icon"><use href="#icon-pin"/></svg><span class="contact-value is-plain">4810 Alder Crest Dr, Plano, TX 75024</span></div>
    <div class="company-bar">Ridgeline Coaching and Behavioral Consulting LLC</div>
  </div>
</section>
</body>
</html>
```